Urine collection cup with and without sterile seal sticker

Hello. We need a urine cup label designed please with

Name:
Date of Birth:
Date:
Time:
Temp℃:
Specimen ID:

Product code: TUB-47
Volume markings (e.g., 30 mL, 60 mL, 90 mL).
Vela Drug Tests logo

Could you please provide one version with the additional sterile sticker extending to the top, and one version without the additional sterile sticker?

```html
<!DOCTYPE html>
<html lang="en">
<head>
<meta charset="utf-8">
<title>Vela Drug Tests – Urine Cup Label</title>
<link rel="stylesheet" href="https://fonts.googleapis.com/css2?family=Arimo:wght@400&family=Open+Sans:wght@400&display=swap">
<style>
  :root {
    --backdrop: #e1f3fd;
    --label-white: #ffffff;
    --brand-navy: #0b2942;
    --field-blue: #3a9ad9;
    --guide-pink: #e8336b;
  }
  html, body {
    margin: 0;
    padding: 0;
    width: 1200px;
    height: 929px;
    overflow: hidden;
    background: var(--backdrop);
  }
  .canvas {
    position: relative;
    width: 1200px;
    height: 929px;
  }
  .dimension-guides {
    position: absolute;
    inset: 0;
  }
  .dimension-text {
    position: absolute;
    font-family: "Open Sans", sans-serif;
    font-size: 11px;
    color: var(--guide-pink);
    white-space: nowrap;
  }
  .dimension-text--height {
    left: 216px;
    top: 447px;
    transform: translate(-50%, -50%) rotate(-90deg);
  }
  .dimension-text--width {
    left: 609px;
    top: 758px;
    transform: translate(-50%, -50%);
  }
  .cup-label {
    position: absolute;
    left: 367px;
    top: 303px;
    width: 484px;
    height: 290px;
    background: var(--label-white);
    border-radius: 13px;
    overflow: hidden;
    font-family: "Arimo", sans-serif;
    color: var(--field-blue);
  }
  .brand-band {
    position: absolute;
    left: 0;
    top: 0;
    width: 56px;
    height: 100%;
    background: var(--brand-navy);
  }
  .brand-name {
    position: absolute;
    left: 28px;
    top: 145px;
    transform: translate(-50%, -50%) rotate(-90deg);
    white-space: nowrap;
    font-family: "Arimo", sans-serif;
    font-weight: 400;
    font-size: 17px;
    color: var(--label-white);
  }
  .field-list {
    position: absolute;
    left: 74px;
    top: 20px;
    width: 391px;
    margin: 0;
    padding: 0;
    list-style: none;
  }
  .field {
    display: flex;
    align-items: baseline;
    height: 38px;
    font-size: 20px;
    line-height: 26px;
  }
  .field-blank {
    flex: 1;
    border-bottom: 1.2px solid var(--field-blue);
    height: 0;
    transform: translateY(2px);
  }
  .field-blank--short {
    flex: 0 0 148px;
    margin-right: 6px;
  }
  .product-line {
    position: absolute;
    left: 74px;
    top: 250px;
    width: 388px;
    display: flex;
    justify-content: space-between;
    font-size: 20px;
    line-height: 26px;
  }
</style>
</head>
<body>
<div class="canvas">
  <svg class="dimension-guides" width="1200" height="929" viewBox="0 0 1200 929" aria-hidden="true">
    <g stroke="#e8336b" stroke-width="1.5" stroke-dasharray="1.5 4.5" fill="none" stroke-linecap="round">
      <line x1="220" y1="303" x2="437" y2="303"/>
      <line x1="220" y1="593" x2="437" y2="593"/>
      <line x1="251" y1="312" x2="251" y2="584"/>
      <line x1="367" y1="565" x2="367" y2="754"/>
      <line x1="851" y1="565" x2="851" y2="754"/>
      <line x1="376" y1="722" x2="842" y2="722"/>
    </g>
    <g fill="#e8336b">
      <polygon points="251,303 245,315 257,315"/>
      <polygon points="251,593 245,581 257,581"/>
      <polygon points="367,722 379,716 379,728"/>
      <polygon points="851,722 839,716 839,728"/>
    </g>
  </svg>
  <span class="dimension-text dimension-text--height">30 mm</span>
  <span class="dimension-text dimension-text--width">50 mm</span>

  <section class="cup-label" aria-label="Urine collection cup label">
    <div class="brand-band">
      <span class="brand-name">Vela Drug Tests</span>
    </div>
    <ul class="field-list">
      <li class="field"><span>Name:</span><span class="field-blank"></span></li>
      <li class="field"><span>Date of Birth:</span><span class="field-blank"></span></li>
      <li class="field"><span>Date:</span><span class="field-blank field-blank--short"></span><span>Time:</span><span class="field-blank"></span></li>
      <li class="field"><span>Temp°C:</span><span class="field-blank"></span></li>
      <li class="field"><span>Specimen ID:</span><span class="field-blank"></span></li>
    </ul>
    <div class="product-line">
      <span>Product code: TUB-47</span>
      <span>90 mL</span>
    </div>
  </section>
</div>
</body>
</html>
```